Ayurvedic Beauty Company in Need of Business Cards

My company is a high-end ayurvedic beauty brand. I need a business card that represents that. The designer should utilize logo and color palette. I want these cards to be printed with the foil accents so keep that in mind.

I have attached the ai of my logo and business card info. As well as, some of the product we are launching soon, they do not have to be on the card.

Be creative and have fun.

Thanks in advance,

Marla

```html
<!DOCTYPE html>
<html lang="en">
<head>
<meta charset="utf-8">
<title>Saffron Veil — Business Cards</title>
<link rel="stylesheet" href="https://fonts.googleapis.com/css2?family=Montserrat:wght@500;600;700&family=Roboto:wght@400;500&display=swap">
<style>
  :root {
    --backdrop: #1c1a1b;
    --plum-light: #7a2a66;
    --plum: #62194f;
    --plum-deep: #44102f;
    --gold: #d6bd86;
    --gold-light: #f3e4b6;
    --gold-dark: #a8894f;
    --ink-light: #f4ecf1;
    --rule: rgba(243, 228, 182, 0.35);
  }
  * { box-sizing: border-box; margin: 0; padding: 0; }
  html, body {
    width: 1200px; height: 1200px; overflow: hidden;
    background: var(--backdrop);
  }
  .canvas {
    position: relative; width: 1200px; height: 1200px;
  }
  .card {
    position: absolute; left: 160px;
    width: 880px; height: 503px;
    border-radius: 22px;
    overflow: hidden;
    background: radial-gradient(ellipse at 40% 35%, var(--plum-light) 0%, var(--plum) 50%, var(--plum-deep) 100%);
    box-shadow: 0 18px 40px rgba(0,0,0,0.5);
  }
  .card--front { top: 70px; }
  .card--back { top: 627px; }

  /* Front */
  .front-brand {
    position: absolute; inset: 0;
    display: flex; flex-direction: column; align-items: center; justify-content: center; gap: 34px;
  }
  .brand-mark {
    width: 150px; height: 150px; border-radius: 50%;
    background: linear-gradient(135deg, var(--gold-light), var(--gold) 55%, var(--gold-dark));
  }
  .brand-name {
    font-family: "Montserrat", sans-serif; font-weight: 600;
    color: var(--gold); letter-spacing: 0.08em;
    font-size: 50px; text-transform: uppercase;
  }

  /* Back */
  .identity {
    position: absolute; left: 60px; top: 60px; width: 330px;
    display: flex; flex-direction: column; align-items: center;
  }
  .identity .brand-mark { width: 130px; height: 130px; }
  .identity .brand-name { font-size: 30px; margin-top: 22px; }
  .person { margin-top: 40px; text-align: center; }
  .person-name {
    font-family: "Montserrat", sans-serif; font-weight: 700;
    color: var(--gold); font-size: 30px; letter-spacing: 0.04em; text-transform: uppercase;
  }
  .person-title {
    font-family: "Roboto", sans-serif; font-weight: 400;
    color: var(--ink-light); font-size: 17px; letter-spacing: 0.1em; margin-top: 4px;
  }
  .contacts {
    position: absolute; left: 420px; top: 90px; width: 360px;
    list-style: none;
  }
  .contact {
    display: flex; align-items: center; gap: 16px;
    padding: 16px 0;
    border-bottom: 1px solid var(--rule);
    font-family: "Roboto", sans-serif; font-size: 19px; color: var(--ink-light);
  }
  .contact:first-child { border-top: 1px solid var(--rule); }
  .contact-icon {
    flex: none; width: 34px; height: 34px; border-radius: 50%;
    background: linear-gradient(135deg, var(--gold-light), var(--gold));
    display: flex; align-items: center; justify-content: center;
  }
  .contact-icon svg { width: 18px; height: 18px; }
  .gold-sweep { position: absolute; right: 0; bottom: 0; }
</style>
</head>
<body>
<main class="canvas">
  <section class="card card--front" aria-label="Card front">
    <div class="front-brand">
      <div class="brand-mark"></div>
      <p class="brand-name">Saffron Veil</p>
    </div>
  </section>

  <section class="card card--back" aria-label="Card back">
    <div class="identity">
      <div class="brand-mark"></div>
      <p class="brand-name">Saffron Veil</p>
      <div class="person">
        <p class="person-name">Marla Vance</p>
        <p class="person-title">CEO</p>
      </div>
    </div>

    <ul class="contacts">
      <li class="contact">
        <span class="contact-icon"><svg viewBox="0 0 24 24"><path fill="#62194f" d="M6.6 10.8a15 15 0 0 0 6.6 6.6l2.2-2.2c.3-.3.7-.4 1-.2 1.1.4 2.3.6 3.6.6.6 0 1 .4 1 1V20c0 .6-.4 1-1 1A17 17 0 0 1 3 4c0-.6.4-1 1-1h3.5c.6 0 1 .4 1 1 0 1.3.2 2.5.6 3.6.1.3 0 .7-.2 1z"/></svg></span>
        1(888) 555-0142
      </li>
      <li class="contact">
        <span class="contact-icon"><svg viewBox="0 0 24 24"><rect x="7" y="2" width="10" height="20" rx="2" fill="none" stroke="#62194f" stroke-width="2"/><circle cx="12" cy="18" r="1.2" fill="#62194f"/></svg></span>
        1(347) 555-0187
      </li>
      <li class="contact">
        <span class="contact-icon"><svg viewBox="0 0 24 24"><rect x="3" y="5" width="18" height="14" rx="1.5" fill="#62194f"/><path d="M3.5 6 12 13l8.5-7" fill="none" stroke="#f3e4b6" stroke-width="1.6"/></svg></span>
        marla@lovesaffronveil.com
      </li>
      <li class="contact">
        <span class="contact-icon"><svg viewBox="0 0 24 24" fill="none" stroke="#62194f" stroke-width="1.6"><circle cx="12" cy="12" r="9"/><ellipse cx="12" cy="12" rx="4" ry="9"/><path d="M3 12h18M5 7h14M5 17h14"/></svg></span>
        www.lovesaffronveil.com
      </li>
    </ul>

    <svg class="gold-sweep" width="880" height="503" viewBox="0 0 880 503" aria-hidden="true">
      <defs>
        <linearGradient id="foil" x1="0" y1="1" x2="1" y2="0">
          <stop offset="0" stop-color="#a8894f"/>
          <stop offset="0.45" stop-color="#f3e4b6"/>
          <stop offset="1" stop-color="#c9ad72"/>
        </linearGradient>
      </defs>
      <path d="M880 20 C 860 260, 800 420, 560 503 L 880 503 Z" fill="url(#foil)"/>
      <path d="M880 60 C 865 280, 810 430, 610 503 L 600 503 C 800 425, 850 270, 868 40 Z" fill="#62194f"/>
    </svg>
  </section>
</main>
</body>
</html>
```